Homepage design for site providing cloud based engineering applications

I need the design for the homepage of a new site providing cloud based engineering applicaitons. The items that must have are provided in the attached pdf file. The layout and colors shown in the attached file is not intened to restrict your design. You should be creative to come up with your best design. We may have many applications. How to show these applicaitons on the homepage would be very important. Anyway, we want our hompage to be simple and clear.

Target Market(s)

Structure engineers(People design bridges, buildings and wharfs etc.)

Industry/Entity Type

Engineering

Requirements
Must have
• See attached pdf file.
Should not have
• No flash will be used.

```html
<!DOCTYPE html>
<html lang="en">
<head>
<meta charset="utf-8">
<title>Skyward Apps – Home</title>
<link rel="stylesheet" href="https://fonts.googleapis.com/css2?family=Ubuntu:wght@300;400;500&display=swap">
<style>
  :root {
    --page-bg: #1b1b1b;
    --header-top: #2a2a2a;
    --header-bottom: #0b0b0b;
    --accent: #4ab4ee;
    --accent-strong: #1f9be6;
    --link: #1a8ad4;
    --ink: #333333;
    --white: #ffffff;
    --strip: #000000;
    --footer-bg: #0a0a0a;
    --eyebrow: #c8391c;
    --tab-bg: #2b2b2b;
  }
  * { box-sizing: border-box; margin: 0; padding: 0; }
  html, body { width: 1200px; height: 840px; overflow: hidden; }
  body {
    position: relative;
    background: radial-gradient(ellipse at 60% 40%, #262626 0%, var(--page-bg) 70%);
    font-family: "Ubuntu", sans-serif;
    color: var(--white);
  }
  .abs { position: absolute; }

  /* Header */
  .site-header {
    position: absolute; left: 0; top: 0; width: 1200px; height: 61px;
    background: linear-gradient(var(--header-top), var(--header-bottom));
    border-bottom: 1px solid #303030;
  }
  .brand { position: absolute; left: 122px; top: 14px; display: flex; align-items: center; gap: 14px; }
  .brand-mark { width: 40px; height: 30px; border: 3px solid var(--accent); border-radius: 50%; }
  .brand-name { font-size: 26px; font-weight: 300; color: var(--white); letter-spacing: 0.2px; }
  .main-nav { position: absolute; right: 138px; top: 22px; display: flex; font-size: 14px; }
  .main-nav a { color: var(--white); text-decoration: none; }
  .main-nav a.is-current { color: var(--accent); }
  .main-nav .sep { color: #777; margin: 0 14px; font-size: 18px; line-height: 16px; }
  .header-rule { left: 121px; top: 62px; width: 968px; height: 4px; background: var(--accent); }
  .account-tab {
    left: 956px; top: 66px; width: 133px; height: 25px; background: var(--tab-bg);
    font-size: 12px; padding: 6px 0 0 8px; color: var(--white); border-radius: 0 0 3px 3px;
  }
  .account-tab::after {
    content: ""; position: absolute; right: 8px; top: 9px;
    border-left: 5px solid transparent; border-right: 5px solid transparent; border-top: 7px solid var(--white);
  }

  /* Intro */
  .headline {
    left: 117px; top: 158px; font-size: 72px; font-weight: 300; line-height: 64px; color: var(--accent);
  }
  .intro {
    left: 123px; top: 312px; width: 390px; font-size: 15px; line-height: 27px; color: var(--white);
  }

  /* Feature card */
  .feature-card { left: 547px; top: 274px; width: 542px; height: 343px; background: var(--white); }
  .card-band { left: 547px; top: 467px; width: 237px; height: 20px; background: #e6e6e6; }
  .device-shot {
    left: 581px; top: 178px; width: 175px; height: 390px; border-radius: 26px 26px 14px 14px;
    background: linear-gradient(180deg, #3a3a3a 0%, #111 30%, #2d6fb0 34%, #5fb04a 58%, #111 62%, #1a1a1a 88%, rgba(200,200,200,0.2) 100%);
  }
  .app-eyebrow { left: 783px; top: 219px; font-size: 14px; color: var(--eyebrow); }
  .app-title { left: 783px; top: 240px; font-size: 19px; color: var(--white); }
  .app-title-rule { left: 783px; top: 268px; width: 150px; height: 5px; background: var(--accent); }
  .app-copy { left: 787px; top: 299px; width: 262px; font-size: 13px; line-height: 22px; color: var(--ink); }
  .app-copy p + p { margin-top: 22px; }
  .more-link { left: 790px; top: 468px; font-size: 14px; font-weight: 500; color: var(--link); }
  .more-link::after {
    content: ""; display: inline-block; margin-left: 8px; vertical-align: 1px;
    border-top: 4px solid transparent; border-bottom: 4px solid transparent; border-left: 6px solid var(--link);
  }
  .actions { left: 587px; top: 563px; display: flex; gap: 6px; }
  .btn {
    height: 30px; padding: 0 17px; font-size: 16px; line-height: 28px; color: var(--white);
    background: linear-gradient(#55c4ff, var(--accent-strong));
    border: 1px solid #1686cb; border-radius: 3px; box-shadow: 0 1px 2px rgba(0,0,0,0.25);
  }
  .btn-trial { width: 107px; } .btn-buy { width: 113px; } .btn-shots { width: 119px; margin-left: 0; } .btn-launch { width: 90px; margin-left: 2px; }
  .slide-arrow { top: 418px; }
  .slide-arrow.prev { left: 512px; }
  .slide-arrow.next { left: 1097px; top: 424px; }

  /* App strip */
  .app-strip { left: 90px; top: 683px; width: 999px; height: 50px; background: var(--strip); }
  .app-thumb { left: 139px; top: 583px; width: 92px; }
  .app-thumb-photo {
    height: 92px; border: 1px solid var(--white);
    background: linear-gradient(160deg, #e0e0e0, #8a8a8a 60%, #2a2a2a);
  }
  .app-thumb-label {
    position: relative; height: 35px; background: var(--accent-strong);
    font-size: 12px; padding: 15px 0 0 7px; color: var(--white);
  }
  .app-thumb-label::before {
    content: ""; position: absolute; left: 4px; top: -1px;
    border-left: 7px solid transparent; border-right: 7px solid transparent; border-top: 10px solid var(--white);
  }
  .strip-dash { top: 708px; width: 88px; height: 4px; background: var(--accent-strong); }

  /* Footer */
  .site-footer {
    left: 0; top: 789px; width: 1200px; height: 51px; background: var(--footer-bg);
    border-top: 1px solid #2a2a2a; font-size: 12px;
  }
  .footer-links { position: absolute; left: 143px; top: 17px; display: flex; gap: 25px; }
  .footer-links a { color: var(--accent); text-decoration: none; }
  .copyright { position: absolute; left: 755px; top: 17px; color: var(--white); }
</style>
</head>
<body>
  <header class="site-header">
    <div class="brand">
      <span class="brand-mark"></span>
      <span class="brand-name">Skyward Apps</span>
    </div>
    <nav class="main-nav">
      <a class="is-current" href="#">Home</a><span class="sep">/</span>
      <a href="#">Products</a><span class="sep">/</span>
      <a href="#">Buy Now</a><span class="sep">/</span>
      <a href="#">Support</a><span class="sep">/</span>
      <a href="#">About Us</a>
    </nav>
  </header>
  <div class="abs header-rule"></div>
  <div class="abs account-tab">Log in or Register</div>

  <h1 class="abs headline">One Platform<br>Many Ideas</h1>
  <p class="abs intro">We’re a small Cloud based application studio, based in London. We build state-of-the art, robust applications for computers and mobile devices.</p>

  <div class="abs feature-card"></div>
  <div class="abs card-band"></div>
  <div class="abs device-shot" role="img" aria-label="Smartphone showing the Par Pulse app screen with a golf ball on grass"></div>
  <p class="abs app-eyebrow">Riverside Golf Club</p>
  <h2 class="abs app-title">Par Pulse App</h2>
  <div class="abs app-title-rule"></div>
  <div class="abs app-copy">
    <p>Lorem ipsum dolor sit amet, consectetur adipiscing elit. Suspendisse sodales ullamcorper aliquet. Nam porta lobortis interdum. Integer sed nibh lacus.</p>
    <p>Nam porta lobortis interdum. Integer sed nibh lacus.</p>
  </div>
  <a class="abs more-link">More Details</a>
  <div class="abs actions">
    <span class="btn btn-trial">Free Trial</span>
    <span class="btn btn-buy">Buy It Now</span>
    <span class="btn btn-shots">Screenshots</span>
    <span class="btn btn-launch">Launch</span>
  </div>
  <svg class="abs slide-arrow prev" width="18" height="34" viewBox="0 0 18 34"><polyline points="16,1 2,17 16,33" fill="none" stroke="#4ab4ee" stroke-width="1.5"/></svg>
  <svg class="abs slide-arrow next" width="18" height="34" viewBox="0 0 18 34"><polyline points="2,1 16,17 2,33" fill="none" stroke="#4ab4ee" stroke-width="1.5"/></svg>

  <div class="abs app-strip"></div>
  <div class="abs app-thumb">
    <div class="app-thumb-photo" role="img" aria-label="Black and white photo of a golfer holding a club"></div>
    <div class="app-thumb-label">Par Pulse</div>
  </div>
  <div class="abs strip-dash" style="left:253px"></div>
  <div class="abs strip-dash" style="left:369px"></div>
  <div class="abs strip-dash" style="left:485px"></div>
  <div class="abs strip-dash" style="left:604px"></div>
  <div class="abs strip-dash" style="left:720px"></div>
  <div class="abs strip-dash" style="left:836px"></div>
  <div class="abs strip-dash" style="left:952px"></div>

  <footer class="abs site-footer">
    <nav class="footer-links">
      <a href="#">Contact Us</a>
      <a href="#">Privacy</a>
      <a href="#">Terms of Use</a>
    </nav>
    <p class="copyright">Copyright 2011 Skyward Apps. All Rights Reserved.</p>
  </footer>
</body>
</html>
```